Redesign of Real Estate Agency Website

We need a redesign for our real estate agency website. Please see attached creative brief.

Target Market(s)

Refer to creative brief.

Industry/Entity Type

Real Estate

Requirements
Must have
• Refer to creative brief.

```html
<!DOCTYPE html>
<html lang="en">
<head>
<meta charset="utf-8">
<title>Inquire About this Property</title>
<link rel="stylesheet" href="https://fonts.googleapis.com/css2?family=Arimo:wght@400;700&family=Source+Sans+3:wght@400;600&display=swap">
<style>
:root{
  --text:#6b6b6b;
  --label:#555;
  --brand:#1a8ad0;
  --accent:#1679c9;
  --required:#d40000;
  --green:#7a9a1a;
  --field-border:#dcdcdc;
  --line:#e3e3e3;
  --panel-end:#f6f6f6;
  --link-line:rgba(255,255,255,.28);
  --white:#fff;
}
*{box-sizing:border-box;margin:0;padding:0}
html,body{width:1200px;height:900px;overflow:hidden;background:var(--white)}
body{position:relative;font-family:Arimo,Arial,sans-serif;font-size:10.4px;color:var(--text)}
.abs{position:absolute}
.nowrap{white-space:nowrap}

/* left sidebar */
.sidebar-box{left:234px;top:-10px;width:237px;height:120px;border:1px solid #e6e2cf;border-radius:4px;background:#fffef8}
.rates{left:280px;top:-10px;width:136px;height:111px;border:1px solid #9a9a9a;border-radius:0 0 5px 5px;background:var(--white);font-size:9px;color:#333;overflow:hidden}
.rates table{width:100%;border-collapse:collapse}
.rates th{font-weight:700;font-size:8.5px;border-bottom:1px solid #aaa;border-right:1px solid #aaa;padding:0 2px;line-height:10px}
.rates th:last-child,.rates td:last-child{border-right:0}
.rates td{height:12px;border-right:1px solid #ccc;border-bottom:1px solid #e2e2e2;text-align:right;padding:0 6px}
.rates td:first-child{text-align:center}
.rates tr:nth-child(even) td{background:#eeeeee}
.rates .stamp{display:flex;justify-content:space-between;padding:4px 6px 0;font-size:9px;color:#444;border-top:1px solid #aaa;height:20px;background:#f0f0f0}
.rates .stamp a{color:#1a3fb0;text-decoration:underline}

/* main panel */
.listing-tail{left:491px;top:0;width:466px;height:89px;background:linear-gradient(#fff 30%,var(--panel-end));border-bottom:1px solid var(--line)}
.listing-tail p{position:absolute;left:29px;top:-8px;line-height:15px;white-space:nowrap}
.listing-tail .must{top:58px;color:var(--accent);font-weight:700}
.inquiry{left:491px;top:90px;width:466px;height:383px;background:linear-gradient(#fff 40%,var(--panel-end));border-bottom:1px solid var(--line)}
.inquiry h2{position:absolute;left:15px;top:13px;font-family:"Source Sans 3",Arial,sans-serif;font-weight:600;font-size:15px;color:var(--brand)}
.intro{position:absolute;left:29px;top:37px;line-height:14.6px;white-space:nowrap}
.btn{position:absolute;border:1px solid #d4d4d4;border-radius:4px;background:linear-gradient(#fff,#ececec);color:var(--green);font-size:10.5px;text-align:center}
.btn-cart{left:31px;top:118px;width:94px;height:20px;line-height:18px}
.note{position:absolute;left:29px;top:148px;line-height:15px;white-space:nowrap}
.req{color:var(--required)}
.label{position:absolute;left:32px;color:var(--label);white-space:nowrap}
.field{position:absolute;left:132px;width:230px;height:22px;border:1px solid var(--field-border);background:linear-gradient(#f4f4f4,#fff)}
.select{color:#bbb;padding:5px 6px;font-size:10px}
.select .arrow{position:absolute;right:-1px;top:-1px;width:24px;height:22px}
.comments{height:55px}
.btn-send{left:268px;top:354px;width:94px;height:20px;line-height:18px;font-weight:700}

/* footer */
.scene-art{left:786px;top:481px;width:97px;height:64px;background:linear-gradient(#2d9de0,#1f86cc);border-radius:40px 40px 4px 4px}
.footer-wave{left:0;top:540px;width:1200px;height:360px}
.col{position:absolute;top:582px;width:176px;color:var(--white)}
.col h3{font-family:"Source Sans 3",Arial,sans-serif;font-weight:600;font-size:14px;letter-spacing:-.1px;line-height:20px;padding-bottom:3px;border-bottom:1px solid var(--link-line);height:24px;white-space:nowrap}
.col ul{list-style:none;padding-top:2px}
.col li{height:17.86px;line-height:17.5px;border-bottom:1px solid var(--link-line);font-size:10.2px;letter-spacing:-.15px;padding-left:1px;white-space:nowrap}
.col li:last-child{border-bottom:0}
.sub{margin-top:29px}
.legal{left:560px;top:863px;width:397px;text-align:right;color:var(--white);font-size:9px;letter-spacing:-.1px;white-space:nowrap}
</style>
</head>
<body>

<div class="abs sidebar-box"></div>
<div class="abs rates">
  <table>
    <tr><th>Currency<br>/Baht</th><th>Bank Notes<br>Buy</th><th><br>Sell</th></tr>
    <tr><td>USD</td><td>29.44</td><td>30.09</td></tr>
    <tr><td>GBP</td><td>47.07</td><td>48.65</td></tr>
    <tr><td>EUR</td><td>41.45</td><td>42.65</td></tr>
    <tr><td>JPY</td><td>36.00</td><td>37.48</td></tr>
    <tr><td>HKD</td><td>3.74</td><td>3.94</td></tr>
  </table>
  <div class="stamp"><span>15 Oct 10 at 14:05</span><a>More&raquo;</a></div>
</div>

<section class="abs listing-tail">
  <p>master bedroom suite with dressing room and en-suite bathroom, family room, dining room,<br>cloakroom, kitchen/breakfast room, separate Asian wet kitchen, laundry room, maids quarter,<br>undercover walkway to elevator.</p>
  <p class="must">A MUST SEE!</p>
</section>

<section class="abs inquiry">
  <h2>Inquire About this Property</h2>
  <p class="intro">To request more information about this property, please provide us with your email address,<br>name and any questions that you might have. We will respond within 24 hours.<br>We look forward to assisting you.<br>To submit an inquiry for multiple properties click "Add to Inquiry Cart". You will be taken the Inquiry<br>Cart page where you can review items and then continue to inquiry form or add more properties.</p>
  <div class="btn btn-cart">Add to Inquery</div>
  <p class="note">Alternatively, to submit an inquiry for this property only, complete the form below and click "Send".<br><span class="req">*</span> indicates a required field.</p>

  <span class="label" style="top:198px">Your name <span class="req">*</span></span>
  <div class="field" style="top:192px"></div>
  <span class="label" style="top:224px">Your email <span class="req">*</span></span>
  <div class="field" style="top:217px"></div>
  <span class="label" style="top:250px">Country of residence</span>
  <div class="field select" style="top:242px">Please select country
    <svg class="arrow" viewBox="0 0 24 22"><rect width="24" height="22" fill="#333"/><path d="M7 7l5 4 5-4M7 11l5 4 5-4" stroke="#fff" stroke-width="1.6" fill="none"/></svg>
  </div>
  <span class="label" style="top:276px">Phone number</span>
  <div class="field" style="top:269px"></div>
  <span class="label" style="top:302px">Comments</span>
  <div class="field comments" style="top:295px"></div>
  <div class="btn btn-send">Send</div>
</section>

<div class="abs scene-art" role="img" aria-label="Illustration of a small house beside a tree"></div>

<svg class="abs footer-wave" viewBox="0 0 1200 360" preserveAspectRatio="none">
  <defs>
    <linearGradient id="sky" x1="0" y1="0" x2="0" y2="1">
      <stop offset="0" stop-color="#2b9bdb"/>
      <stop offset="0.35" stop-color="#2787c6"/>
      <stop offset="1" stop-color="#1c6aa0"/>
    </linearGradient>
  </defs>
  <path d="M0 18 L234 18 C360 34 560 42 700 20 C760 10 800 4 860 6 C920 8 940 18 960 18 L1200 18 L1200 360 L0 360Z" fill="url(#sky)"/>
</svg>

<nav class="col" style="left:234px">
  <h3>Phuket Real Estate For Sale</h3>
  <ul>
    <li>Phuket property for sale index</li><li>Search property for sale in phuket</li>
    <li>Apartments &amp; condos for sale in phuket</li><li>Villas &amp; houses for sale in phuket</li>
    <li>Land for sale in phuket</li><li>Commercial property for sale in phuket</li>
    <li>Luxury property for sale</li><li>Property for sale map</li>
    <li>Property buyer's guide for phuket</li><li>Why phuket?</li>
    <li>Property ownership rights</li><li>Property taxes &amp; fees</li>
    <li>Land titles</li><li>Land units</li><li>Property faq</li>
  </ul>
</nav>
<nav class="col" style="left:417px">
  <h3>Phuket Property For Rent</h3>
  <ul>
    <li>Phuket property for rent index</li><li>Search property for rent in phuket</li>
    <li>Phuket holiday rentals</li><li>Holiday villas</li><li>Luxury villas</li>
    <li>Cheap villas</li><li>Holiday apartments</li><li>Holiday rentals booking guide</li>
    <li>Holiday rentals faq</li><li>Terms &amp; conditions</li><li>Samui holiday rentals</li>
    <li>Phuket long-term rentals</li><li>Long-term villas &amp; houses</li>
    <li>Long-term apartments</li><li>Property for rent map</li>
  </ul>
</nav>
<nav class="col" style="left:600px">
  <h3>Site Links</h3>
  <ul>
    <li>Baylight.net real estate index</li><li>Privacy policy</li><li>Disclaimer</li><li>Site map</li>
  </ul>
  <h3 class="sub">About Baylight.net Real Estate</h3>
  <ul>
    <li>About us</li><li>Contact us</li><li>List your property</li><li>Sselling your property</li>
  </ul>
</nav>
<nav class="col" style="left:782px">
  <h3>Phuket Info</h3>
  <ul>
    <li>Baylight.net homepage</li><li>Travel info</li><li>Tours</li><li>Dining &amp; nightlife</li>
    <li>Expats</li><li>Directory</li><li>Classified ads</li><li>Hotels</li>
  </ul>
</nav>

<p class="abs legal">Phuket Real Estate from Baylight.net | Copyright &copy; Baylight.net 2008. All Rights Reserved</p>

</body>
</html>
```